Infectious Diseases Research Laboratory Needs Business Card

We need a business card for an academic research laboratory based in Kansas City called VELKOR. The full lab name is Microbe Exposure Kinetics/Response Modeling Integrated Study Laboratory, but this does not need to be incorporated. We study novel ways to optimize the treatment of multidrug-resistant bacterial infections ("superbugs") throughout the entire biomedical research spectrum (from benchtop to bedside). The name VELKOR is not only an acronym for our lab name, but also represents our desire to make discoveries and explore the unknown (the stars, if you well). It also serves as an ode to the state of Kansas motto where we are based, ad astra per aspera ("to the stars, through difficulty").

Target Market(s)

Pharmaceutical companies, researchers

Industry/Entity Type

Pharmaceutical

Contact Information for Business Card

The business card should incorporate and complement our new logo (see uploaded files). Double-sided designs are preferred. Looking for something modern, but professional.

Font styles to use
Sans Serif

Requirements
Must have
• Double-sided. One side would ideally be a solid color incorporating logo and the other should also have the logo (smaller), but incorporate staff information.
• Color codes:
• Red: #F04C51
• Blue: #3477B5
• Gray: #808285

```html
<!DOCTYPE html>
<html lang="en">
<head>
<meta charset="utf-8">
<title>VELKOR Business Card</title>
<link href="https://fonts.googleapis.com/css2?family=Josefin+Sans:wght@400;600&family=Montserrat:wght@400;500&display=swap" rel="stylesheet">
<style>
  :root {
    --red: #F04C51;
    --red-deep: #E0414A;
    --blue: #3477B5;
    --gray: #808285;
    --ink: #3a3b3d;
    --paper: #ffffff;
    --stage: #161616;
  }
  * { box-sizing: border-box; margin: 0; padding: 0; }
  html, body {
    width: 1200px; height: 1000px; overflow: hidden;
    background: var(--stage);
  }
  .canvas { position: relative; width: 1200px; height: 1000px; }

  .card {
    position: absolute;
    width: 520px; height: 300px;
    border-radius: 22px;
    overflow: hidden;
    box-shadow: 0 18px 40px rgba(0,0,0,0.55);
  }

  /* Front: staff side */
  .card--front { left: 60px; top: 230px; background: var(--paper); }
  .front__brand {
    position: absolute; left: 36px; top: 34px;
    display: flex; align-items: center; gap: 12px;
  }
  .brand__dot {
    width: 26px; height: 26px; border-radius: 50%;
    background: var(--red);
  }
  .brand__name {
    font-family: "Josefin Sans", sans-serif;
    font-weight: 600; font-size: 34px; letter-spacing: 3px;
    color: var(--red); line-height: 1;
    padding-top: 5px;
  }
  .staff { position: absolute; left: 36px; top: 112px; }
  .staff__name {
    font-family: "Josefin Sans", sans-serif; font-weight: 600;
    font-size: 21px; letter-spacing: 0.5px; color: var(--blue);
  }
  .staff__name .staff__surname { color: var(--red); }
  .staff__role {
    font-family: "Montserrat", sans-serif; font-size: 11px;
    letter-spacing: 1px; color: var(--gray); margin-top: 2px;
  }
  .contact {
    position: absolute; left: 36px; top: 176px;
    font-family: "Montserrat", sans-serif; font-size: 13px;
    color: var(--ink); line-height: 1.55;
  }
  .front__art {
    position: absolute; right: 0; top: 60px;
    width: 170px; height: 170px;
    background: radial-gradient(circle at 40% 40%, var(--red) 0%, rgba(240,76,81,0.7) 35%, rgba(52,119,181,0.85) 75%, var(--blue) 100%);
    border-radius: 85px 0 0 85px;
  }
  .front__web {
    position: absolute; right: 36px; bottom: 30px;
    font-family: "Josefin Sans", sans-serif; font-weight: 600;
    font-size: 18px; letter-spacing: 2px; color: var(--blue);
  }

  /* Back: solid colour side */
  .card--back {
    left: 620px; top: 450px;
    background: linear-gradient(135deg, #F25A5E 0%, var(--red) 50%, var(--red-deep) 100%);
  }
  .back__surface {
    position: absolute; inset: 0;
    background: radial-gradient(ellipse at 30% 35%, rgba(255,255,255,0.06), rgba(0,0,0,0.05) 70%);
  }
  .back__brand {
    position: absolute; inset: 0;
    display: flex; align-items: center; justify-content: center; gap: 20px;
  }
  .back__brand .brand__dot { width: 48px; height: 48px; background: var(--paper); }
  .back__brand .brand__name {
    color: var(--paper); font-size: 64px; letter-spacing: 8px; padding-top: 10px;
  }
</style>
</head>
<body>
<main class="canvas">
  <section class="card card--front" aria-label="Business card, staff side">
    <div class="front__brand">
      <span class="brand__dot"></span>
      <span class="brand__name">VELKOR</span>
    </div>
    <div class="staff">
      <p class="staff__name">LOREM <span class="staff__surname">IPSUM</span></p>
      <p class="staff__role">MANAGER</p>
    </div>
    <div class="contact">
      <p>+12 345 67890</p>
      <p>email@domain.com</p>
    </div>
    <div class="front__art" role="img" aria-label="Cluster of red and blue bubbles decoration"></div>
    <p class="front__web">WWW.VELKOR.COM</p>
  </section>

  <section class="card card--back" aria-label="Business card, brand side">
    <div class="back__surface" role="img" aria-label="Faint tone-on-tone bubble pattern on red"></div>
    <div class="back__brand">
      <span class="brand__dot"></span>
      <span class="brand__name">VELKOR</span>
    </div>
  </section>
</main>
</body>
</html>
```